EVACUATION SIGNS FOR CABINS

ATTACHED ARE EVACUATION PLANS FOR OUR CABINS.
1. IS A BLANK EVACUTION SIGN & DIAGRAM FOR YOU TO ADD THE THREE DIFFERENT TYPES OF CABINS WE HAVE.
2. DESIGN, A EVACUTION SIGN & DIAGRAM FOR EACH CABIN STYLE.
WITH LEGEND ON EACH ONE SHOWING WHAT IS IN EACH CABIN FOR FIRE SAFETY.

```html
<!DOCTYPE html>
<html lang="en">
<head>
<meta charset="utf-8">
<title>Evacuation Sign &amp; Diagram – Cabins</title>
<link href="https://fonts.googleapis.com/css2?family=Arimo:wght@400;700&family=Tinos:wght@400;700&display=swap" rel="stylesheet">
<style>
:root{
  --frame-blue:#1a1ae6;
  --alarm-red:#e8141b;
  --exit-green:#1f9a3a;
  --path-green:#7cc242;
  --ink:#000;
  --text-blue:#1a1ae6;
  --plan-grey:#d9d9d9;
  --paper:#fff;
}
*{box-sizing:border-box;margin:0;padding:0}
html,body{width:842px;height:1200px;overflow:hidden;background:var(--paper)}
body{font-family:"Arimo",Arial,sans-serif;color:var(--ink);position:relative}
.sign-frame{position:absolute;left:4px;top:16px;width:826px;height:1170px;border:5px solid var(--frame-blue)}
.abs{position:absolute}
.sign-title{left:0;width:842px;top:64px;text-align:center;color:var(--alarm-red);font-weight:700;font-size:29px;letter-spacing:.3px}
.park-name{left:0;width:842px;top:100px;text-align:center;font-weight:700;font-size:15px}
.park-address{left:0;width:842px;top:118px;text-align:center;font-weight:700;font-size:11px}
.section-title{left:0;width:842px;top:186px;text-align:center;font-weight:700;font-size:20px}
.plan-legend{left:68px;top:307px;width:158px;height:174px;border:1px solid #555;background:var(--paper);font-family:"Tinos","Times New Roman",serif;font-size:12px;padding:6px 8px}
.plan-legend .row{position:absolute;left:8px}
.floor-plan{left:232px;top:307px;width:500px;height:176px;background:var(--plan-grey);border:1px solid #666}
.panel{position:absolute;border:3px solid var(--ink);background:var(--paper);overflow:hidden}
.panel h2{font-size:13px;color:var(--alarm-red);text-align:center;text-decoration:underline;font-weight:700;margin-top:6px}
.procedures{left:72px;top:670px;width:460px;height:156px;padding:0 8px;font-size:7px;line-height:1.18}
.procedures h2{margin-bottom:4px}
.procedures .stage{color:var(--alarm-red);font-weight:700;font-size:8px;margin-top:2px}
.procedures .stage b{color:var(--text-blue)}
.procedures p{margin-bottom:1px}
.safety{left:543px;top:670px;width:270px;height:156px;padding:0 10px;font-size:9px}
.safety h2{color:var(--text-blue);text-decoration:none}
.safety ul{list-style:none;margin-top:4px}
.safety li{padding-left:14px;position:relative;margin-bottom:3px;line-height:1.2}
.safety li::before{content:"";position:absolute;left:0;top:2px;width:7px;height:7px;border:1px solid var(--ink)}
.safety .em{color:var(--text-blue);font-weight:700}
.mobility{position:absolute;left:8px;top:78px;width:178px;border:1px solid var(--ink);padding:4px 6px;font-family:"Tinos","Times New Roman",serif;font-weight:700;font-size:9px;line-height:1.3}
.access-icon{position:absolute;left:196px;top:80px;width:54px;height:54px}
.extinguisher-op{left:72px;top:832px;width:288px;height:152px;padding:0 10px;font-size:8px}
.extinguisher-op ul{list-style:none;margin:6px 0 0 12px}
.extinguisher-op li{margin-bottom:1px}
.extinguisher-op li::before{content:"➢ ";}
.extinguisher-op .pass li{margin-left:16px}
.extinguisher-op .pass li::before{content:"□ "}
.extinguisher-op .closing{margin-top:4px;white-space:nowrap}
.equipment{left:72px;top:990px;width:288px;height:158px;padding:0 8px;font-size:8.5px;text-align:center}
.equipment .lead{margin-top:14px;font-size:10px}
.equipment .type{margin-top:10px;font-weight:700;font-size:11px;white-space:nowrap}
.equipment .check{margin-top:10px;display:flex;justify-content:center;align-items:center;gap:8px}
.equipment .warn{margin-top:10px;text-align:left}
.icon-key{left:370px;top:832px;width:163px;height:316px;padding:6px 6px}
.key-row{display:flex;align-items:center;height:24.5px}
.key-row svg{width:26px;height:20px;flex:none}
.key-row span{margin-left:8px;border:1px solid var(--ink);font-size:6.5px;padding:3px 4px;width:100px;line-height:1.1}
.race{left:543px;top:832px;width:270px;height:316px;font-family:"Tinos","Times New Roman",serif;padding:10px 18px}
.race-head{border:1px solid var(--ink);padding:4px 6px;margin:4px 0 22px 0}
.race-head .big{color:var(--alarm-red);font-size:22px;letter-spacing:-1px}
.race-head .sub{color:var(--text-blue);font-size:9px;padding-left:14px}
.race-step{margin-bottom:12px}
.race-step .word{color:var(--alarm-red);font-size:19px;letter-spacing:-1px;white-space:nowrap}
.race-step .word b{font-size:34px;font-weight:400}
.race-step .note{font-size:6.5px;padding-left:28px;margin-top:-4px}
.race-step .note em{color:var(--exit-green);font-style:normal}
</style>
</head>
<body>
<div class="sign-frame"></div>

<h1 class="abs sign-title">EVACUATION SIGN &amp; DIAGRAM</h1>
<div class="abs park-name">HARBOUR GUM HOLIDAY PARK</div>
<div class="abs park-address">212 COASTAL DRIVE, MARLIN BAY, QLD. 4710</div>
<div class="abs section-title">CABINS</div>

<svg class="abs" style="left:232px;top:282px" width="520" height="210" aria-hidden="true">
  <g stroke="#000" stroke-width="1.5" fill="#000">
    <line x1="8" y1="10" x2="406" y2="10"/><path d="M0 10l9-4v8z"/><path d="M414 10l-9-4v8z"/>
    <line x1="432" y1="10" x2="492" y2="10"/><path d="M424 10l9-4v8z"/><path d="M500 10l-9-4v8z"/>
    <line x1="514" y1="33" x2="514" y2="193"/><path d="M514 25l-4 9h8z"/><path d="M514 201l-4-9h8z"/>
  </g>
</svg>

<div class="abs plan-legend">
  <div class="row" style="top:6px">LEGEND</div>
  <div class="row" style="top:44px">Exit Sign -</div>
  <svg class="abs" style="left:96px;top:34px" width="46" height="20"><rect width="46" height="20" fill="var(--exit-green)"/><text x="23" y="13" font-size="7" fill="#fff" text-anchor="middle" font-family="Arimo,sans-serif">EXIT</text></svg>
  <div class="row" style="top:80px">Exit Path -</div>
  <svg class="abs" style="left:90px;top:76px" width="56" height="14"><line x1="0" y1="7" x2="46" y2="7" stroke="var(--alarm-red)" stroke-width="4"/><path d="M56 7l-12-6v12z" fill="var(--alarm-red)"/></svg>
  <div class="row" style="top:112px">Fire Blanket –</div>
  <svg class="abs" style="left:106px;top:102px" width="14" height="28"><rect x="1" y="1" width="12" height="26" rx="5" fill="var(--alarm-red)" stroke="#000" stroke-width=".5"/></svg>
  <div class="row" style="top:144px">Fire Alarms -</div>
  <svg class="abs" style="left:104px;top:142px" width="18" height="12"><ellipse cx="9" cy="4" rx="8" ry="3" fill="#fff" stroke="#000"/><path d="M1 4v4a8 3 0 0 0 16 0V4" fill="#fff" stroke="#000"/></svg>
</div>

<div class="abs floor-plan" role="img" aria-label="Cabin floor plan: bed, robes, kitchenette, bathroom and deck with red exit path to the exit door, fire blanket and smoke alarm positions"></div>

<svg class="abs" style="left:30px;top:604px" width="700" height="40" aria-hidden="true">
  <g fill="var(--alarm-red)" stroke="#000" stroke-width=".6">
    <rect x="4" y="10" width="12" height="28" rx="4"/><rect x="30" y="10" width="12" height="28" rx="4"/><rect x="56" y="10" width="12" height="28" rx="4"/>
  </g>
  <g stroke="#000" fill="none" stroke-width="1.2"><path d="M10 10V4h-6M36 10V4h-6M62 10V4h-6"/></g>
  <rect x="232" y="10" width="44" height="22" fill="var(--exit-green)"/><text x="254" y="24" font-size="7" fill="#fff" text-anchor="middle" font-family="Arimo,sans-serif">AA</text>
  <line x1="302" y1="21" x2="336" y2="21" stroke="var(--path-green)" stroke-width="4"/>
  <path d="M355 14h22v-7l13 14-13 14v-7h-22z" fill="var(--path-green)" stroke="#555"/>
  <rect x="404" y="8" width="28" height="26" fill="#222"/><path d="M410 28l8-8 3 3 6-9" stroke="#f5b800" stroke-width="3" fill="none"/>
  <rect x="442" y="8" width="30" height="26" fill="var(--exit-green)"/><path d="M454 13h6v5h5v6h-5v5h-6v-5h-5v-6h5z" fill="#fff"/>
  <rect x="480" y="8" width="30" height="26" fill="var(--alarm-red)"/><text x="495" y="26" font-size="13" font-weight="700" fill="#fff" text-anchor="middle" font-family="Arimo,sans-serif">FB</text>
  <circle cx="533" cy="21" r="13" fill="var(--alarm-red)"/><circle cx="533" cy="21" r="6" fill="none" stroke="#fff" stroke-width="2"/>
  <rect x="554" y="8" width="36" height="26" fill="var(--exit-green)"/><text x="572" y="26" font-size="12" font-weight="700" fill="#fff" text-anchor="middle" font-family="Arimo,sans-serif">EXIT</text>
  <rect x="600" y="8" width="26" height="26" fill="var(--alarm-red)"/><text x="613" y="19" font-size="4" fill="#fff" text-anchor="middle" font-family="Arimo,sans-serif">FIRE</text><text x="613" y="25" font-size="4" fill="#fff" text-anchor="middle" font-family="Arimo,sans-serif">PANEL</text>
  <rect x="638" y="10" width="24" height="22" fill="var(--alarm-red)"/><rect x="644" y="16" width="12" height="10" fill="#fff"/>
</svg>

<section class="panel procedures">
  <h2>EVACUATION PROCEDURES</h2>
  <p class="stage">STAGE 1:- <b>Removal of people from the immediate Danger Area</b></p>
  <p>Occupants and staff in the immediate danger area are to assemble a safe distance away from the fire and smoke. When the area has been checked all doors and windows should be closed to contain fire.</p>
  <p class="stage">STAGE 2:- <b>Removal to a Safe Area</b></p>
  <p>If the severity of the smoke or fire warrants further evacuation, occupants should be moved through fire / smoke doors to a safe area.</p>
  <p class="stage">STAGE 3:- <b>Complete Evacuation of Entire Complex</b></p>
  <p>Should the emergency demand evacuation of the whole complex, the fire warden directs everyone along the nearest safe route to the ASSEMBLY AREA.</p>
  <p class="stage">STAGE 4:- <b>Roll Call.</b></p>
  <p>To be conducted as soon as possible and to ensure all persons are accounted for. Report all missing persons to <span style="color:var(--alarm-red);font-weight:700">FIRE OFFICERS.</span></p>
  <p class="stage">STAGE 5:- <span style="color:var(--exit-green)">ASSEMBLY AREA</span></p>
</section>

<section class="panel safety">
  <h2>SAFETY MEASURES</h2>
  <ul>
    <li>Always turn off all electrical appliances and shut all doors.</li>
    <li>Your first role is life safety. Only attempt to extinguish fire <span class="em">IF SAFE TO DO SO.</span></li>
  </ul>
  <div class="mobility">Mobility impaired persons should evacuate immediately on hearing the fire alarm assisted by a nominated person.</div>
  <svg class="access-icon" viewBox="0 0 56 56" aria-label="Accessibility symbol" role="img"><rect width="56" height="56" fill="#fff" stroke="#000" stroke-width="2"/><circle cx="26" cy="11" r="4"/><path d="M25 17v15h13l5 11" stroke="#000" stroke-width="4" fill="none"/><path d="M21 26a11 11 0 1 0 14 14" stroke="#000" stroke-width="3" fill="none"/></svg>
</section>

<section class="panel extinguisher-op">
  <h2>FIRE EXTINGUISHER OPERATION</h2>
  <ul>
    <li>Stand well back from fire (3 M)</li>
    <li>Always face the fire with your back to a clear doorway</li>
    <li>Always be in pairs.</li>
    <li>Use the PASS method
      <ul class="pass" style="margin:1px 0 0 0">
        <li>P - pull the pin</li>
        <li>A - aim at edge of fire</li>
        <li>S - squeeze the handle</li>
        <li>S - sweep the fire</li>
      </ul>
    </li>
  </ul>
  <p class="closing">As the fire diminishes, slowly move closer towards the FIRE staying 1 m</p>
</section>

<section class="panel equipment">
  <h2>FIRE FIGHTING EQUIPMENT</h2>
  <p class="lead">Installed in this building are:</p>
  <p class="type">Dry Powder Extinguishers (red with white band)</p>
  <p class="check">Check the Extinguisher label for instructions. <svg width="12" height="22" aria-hidden="true"><rect x="2" y="4" width="8" height="18" rx="3" fill="var(--alarm-red)"/><rect x="2" y="10" width="8" height="3" fill="#fff"/><path d="M6 4V1H1" stroke="#000" fill="none"/></svg></p>
  <p class="warn">Under no circumstances should you use water on or near live electrical equipment.</p>
</section>

<section class="panel icon-key">
  <div class="key-row"><svg viewBox="0 0 28 22"><circle cx="14" cy="11" r="10" fill="var(--alarm-red)"/><circle cx="14" cy="11" r="5" fill="none" stroke="#fff" stroke-width="2"/></svg><span>HOSE REEL</span></div>
  <div class="key-row"><svg viewBox="0 0 28 22"><rect x="4" width="20" height="22" fill="var(--alarm-red)"/><rect x="8" y="6" width="12" height="6" fill="#fff"/></svg><span>FIRE INDICATOR PANEL</span></div>
  <div class="key-row"><svg viewBox="0 0 28 22"><rect x="4" width="20" height="22" fill="var(--alarm-red)"/><rect x="9" y="6" width="10" height="10" fill="#fff"/></svg><span>MANUAL CALL POINT</span></div>
  <div class="key-row"><svg viewBox="0 0 28 22"><rect x="10" y="4" width="8" height="18" rx="3" fill="var(--alarm-red)"/><path d="M14 4V1h-5" stroke="#000" fill="none"/></svg><span>EXTINGUISHER</span></div>
  <div class="key-row"><svg viewBox="0 0 28 22"><rect x="2" width="24" height="22" fill="var(--alarm-red)"/><text x="14" y="15" font-size="11" font-weight="700" fill="#fff" text-anchor="middle" font-family="Arimo,sans-serif">FB</text></svg><span>FIRE BLANKET</span></div>
  <div class="key-row"><svg viewBox="0 0 28 22"><rect x="2" width="24" height="22" fill="var(--exit-green)"/><path d="M11 4h6v4h4v6h-4v4h-6v-4h-4V8h4z" fill="#fff"/></svg><span>FIRST AID</span></div>
  <div class="key-row"><svg viewBox="0 0 28 22"><rect x="4" y="1" width="20" height="20" fill="#fff" stroke="#000"/></svg><span>SWITCH BOARD</span></div>
  <div class="key-row"><svg viewBox="0 0 28 22"><rect width="28" height="22" fill="var(--exit-green)"/><text x="14" y="15" font-size="10" font-weight="700" fill="#fff" text-anchor="middle" font-family="Arimo,sans-serif">EXIT</text></svg><span>EXIT SIGN</span></div>
  <div class="key-row"><svg viewBox="0 0 28 22"><line x1="0" y1="11" x2="28" y2="11" stroke="var(--path-green)" stroke-width="4"/></svg><span>PATH OF EXIT</span></div>
  <div class="key-row"><svg viewBox="0 0 28 22"><line x1="0" y1="11" x2="28" y2="11" stroke="var(--path-green)" stroke-width="4"/></svg><span>MAIN PATH</span></div>
  <div class="key-row"><svg viewBox="0 0 28 22"><g fill="#c8b400"><circle cx="3" cy="11" r="2.5"/><circle cx="10" cy="11" r="2.5"/><circle cx="17" cy="11" r="2.5"/><circle cx="24" cy="11" r="2.5"/></g></svg><span>ALTERNATE PATH</span></div>
  <div class="key-row"><svg viewBox="0 0 28 22"><rect width="28" height="22" fill="var(--exit-green)"/><text x="14" y="14" font-size="7" fill="#fff" text-anchor="middle" font-family="Arimo,sans-serif">AA</text></svg><span>ASSEMBLY AREA</span></div>
</section>

<section class="panel race">
  <div class="race-head">
    <div class="big">IN CASE OF FIRE</div>
    <div class="sub">FIRE / EVACUATION PROCEDURES</div>
  </div>
  <div class="race-step"><div class="word"><b>R</b>EMOVE PEOPLE</div><div class="note">IF IN DANGER TO THE <em>ASSEMBLY POINT</em></div></div>
  <div class="race-step"><div class="word"><b>A</b>LERT THE FIRE SERVICE</div><div class="note">NEARBY RESIDENCE AND MEMBERS OF THE PUBLIC</div></div>
  <div class="race-step"><div class="word"><b>C</b>ONFINE FIRE &amp; SMOKE</div><div class="note">CLOSE ALL WINDOWS &amp; DOORS (IF SAFE TO DO SO)</div></div>
  <div class="race-step"><div class="word"><b>E</b>XTINGUISH</div><div class="note">AND CONTROL THE FIRE (IF SAFE TO DO SO)</div></div>
</section>
</body>
</html>
```